CoveysArmsPersonal

I am a cutting edge, top of the line gun store. We are expanding faster than we can keep up. We offer: Gunsmithing, Transfers, Concealed Carry, Machine Guns, Suppressors. My colors are reflected in my logo. Red, black and white. I like a clean design that gets the point across. I was trying to find a plastic business card, but will settle with a high quality paper product.

Contact Information for Business Card

Dwayne Covey - Owner
620-514-8826 (Cell)
Covey's Range Outfitters
1847 E. Hwy 9
Brackton, KS 67462
sales@coveysrangeoutfitters.com
coveysrangeoutfitters.com

```html
<!DOCTYPE html>
<html lang="en">
<head>
<meta charset="utf-8">
<title>Covey's Range Outfitters – Business Card</title>
<link rel="stylesheet" href="https://fonts.googleapis.com/css2?family=Open+Sans:wght@400;600;700&display=swap">
<style>
  :root {
    --bg-top: #5a6170;
    --bg-bottom: #7f8796;
    --card-black: #262626;
    --card-black-edge: #1d1d1d;
    --card-white: #ffffff;
    --accent-red: #9b1c24;
    --text-light: #f2f2f2;
    --text-dark: #2b2b2b;
    --text-muted: #555555;
  }
  * { box-sizing: border-box; margin: 0; padding: 0; }
  html, body {
    width: 1200px; height: 1023px; overflow: hidden;
  }
  body {
    background: linear-gradient(180deg, var(--bg-top), var(--bg-bottom));
    font-family: "Open Sans", Arial, sans-serif;
    position: relative;
  }
  .card {
    position: absolute;
    width: 580px; height: 330px;
    border-radius: 22px;
    overflow: hidden;
    box-shadow: 0 18px 40px rgba(0,0,0,0.35);
  }

  /* Front */
  .card--front {
    left: 70px; top: 110px;
    background: radial-gradient(ellipse at 50% 40%, #2e2e2e, var(--card-black-edge));
    display: flex; align-items: center; justify-content: center;
  }
  .brand {
    display: flex; align-items: center; gap: 16px;
    font-weight: 600; letter-spacing: 0.12em; text-transform: uppercase;
    white-space: nowrap;
  }
  .brand__mark { width: 26px; height: 26px; flex: none; }
  .brand--front { color: var(--text-light); font-size: 26px; }
  .brand--front .brand__mark { background: var(--text-light); }

  /* Back */
  .card--back {
    left: 550px; top: 560px;
    background: var(--card-white);
  }
  .back__identity {
    position: absolute; left: 34px; top: 136px;
  }
  .back__name {
    color: var(--accent-red); font-weight: 700; font-size: 26px; line-height: 1.1;
  }
  .back__title {
    color: var(--text-muted); font-size: 15px; margin-top: 2px;
  }
  .brand--back {
    position: absolute; right: 34px; top: 148px;
    color: var(--text-dark); font-size: 14px; gap: 10px;
  }
  .brand--back .brand__mark { width: 16px; height: 16px; background: var(--accent-red); }

  .back__band {
    position: absolute; left: 0; right: 0; bottom: 0; height: 124px;
    background: var(--card-black);
    border-top: 5px solid var(--accent-red);
  }
  .back__band-notch {
    position: absolute; left: 52px; top: -5px;
    width: 0; height: 0;
    border-left: 9px solid transparent; border-right: 9px solid transparent;
    border-top: 10px solid var(--card-white);
  }
  .contact-list {
    position: absolute; left: 30px; top: 26px;
    list-style: none; color: var(--text-light); font-size: 15px; line-height: 24px;
  }
  .contact-list li { display: flex; align-items: center; gap: 10px; }
  .contact-list svg { width: 12px; height: 12px; flex: none; }
  .address {
    position: absolute; right: 26px; top: 58px;
    color: var(--text-light); font-size: 15px; line-height: 22px; text-align: right;
    display: flex; align-items: flex-end; gap: 8px; font-style: normal;
  }
  .address svg { width: 11px; height: 15px; flex: none; margin-bottom: 4px; }
</style>
</head>
<body>

  <section class="card card--front" aria-label="Business card front">
    <div class="brand brand--front">
      <span class="brand__mark"></span>
      <span class="brand__name">Covey's Range Outfitters</span>
    </div>
  </section>

  <section class="card card--back" aria-label="Business card back">
    <div class="back__identity">
      <p class="back__name">Dwayne Covey</p>
      <p class="back__title">Owner</p>
    </div>

    <div class="brand brand--back">
      <span class="brand__mark"></span>
      <span class="brand__name">Covey's Range Outfitters</span>
    </div>

    <div class="back__band">
      <span class="back__band-notch"></span>
      <ul class="contact-list">
        <li>
          <svg viewBox="0 0 12 12" aria-hidden="true"><rect x="3" y="0.5" width="6" height="11" rx="1.2" fill="none" stroke="#f2f2f2" stroke-width="1.2"/><circle cx="6" cy="9.5" r="0.8" fill="#f2f2f2"/></svg>
          <span>620-514-8826</span>
        </li>
        <li>
          <svg viewBox="0 0 12 12" aria-hidden="true"><rect x="0.6" y="2" width="10.8" height="8" fill="none" stroke="#f2f2f2" stroke-width="1.2"/><path d="M0.6 2 L6 6.5 L11.4 2" fill="none" stroke="#f2f2f2" stroke-width="1.2"/></svg>
          <span>sales@coveysrangeoutfitters.com</span>
        </li>
        <li>
          <svg viewBox="0 0 12 12" aria-hidden="true"><circle cx="6" cy="6" r="5.2" fill="none" stroke="#f2f2f2" stroke-width="1.2"/><ellipse cx="6" cy="6" rx="2.2" ry="5.2" fill="none" stroke="#f2f2f2" stroke-width="1"/><line x1="0.8" y1="6" x2="11.2" y2="6" stroke="#f2f2f2" stroke-width="1"/></svg>
          <span>www.coveysrangeoutfitters.com</span>
        </li>
      </ul>
      <address class="address">
        <span>Covey's Range Outfitters 1847 E.<br>Hwy 9 Brackton, KS 67462</span>
        <svg viewBox="0 0 11 15" aria-hidden="true"><path d="M5.5 0.5 A5 5 0 0 1 10.5 5.5 C10.5 9 5.5 14.5 5.5 14.5 C5.5 14.5 0.5 9 0.5 5.5 A5 5 0 0 1 5.5 0.5 Z" fill="#f2f2f2"/><circle cx="5.5" cy="5.5" r="1.8" fill="#262626"/></svg>
      </address>
    </div>
  </section>

</body>
</html>
```